Retainer Care Instructions

Please make this PDF - more modern and easy to read for patients. Our demographic is predominately adolescents. All the information is important and text needs to remain relatively the same - can be simplified. Here is a link to care instructions that look nice https://www.brightpath-grins.com/resources

Target Market(s)

Parents and Children

Industry/Entity Type

Orthodontics

Colors
0054AA
0677BA
7BADD7
CADEEF
E8F1F8

Requirements
Must have
• Simple and clear
Nice to have
• Add graphics and images to look more modern
Should not have
• Graphics to demonstrate

```html
<!DOCTYPE html>
<html lang="en">
<head>
<meta charset="utf-8">
<title>Looking After Your Retainers</title>
<link rel="stylesheet" href="https://fonts.googleapis.com/css2?family=Montserrat:wght@700;800;900&family=Inter:wght@400;500;700&display=swap">
<style>
:root{
  --page-bg:#d3e0e9;
  --card:#ffffff;
  --brand:#009ddc;
  --ink:#111111;
  --rule:#b9b9b9;
  --logo-grey:#9d9fa2;
}
*{margin:0;padding:0;box-sizing:border-box}
html,body{width:1200px;height:2279px;overflow:hidden}
body{background:var(--page-bg);font-family:"Inter",sans-serif;color:var(--ink);position:relative}
.card{position:absolute;left:125px;top:93px;width:950px;height:2093px;background:var(--card)}
.abs{position:absolute}
.header-band{left:125px;top:93px;width:950px;height:276px;background:var(--brand)}
.header-pointer{left:283px;top:368px}
.page-title{left:125px;top:183px;width:950px;text-align:center;color:#fff;font-family:"Montserrat",sans-serif;font-weight:900;font-size:55px;line-height:68px;letter-spacing:1px}
.intro-box{left:202px;top:428px;width:796px;height:250px;border:2px dashed var(--brand)}
.heading{font-family:"Montserrat",sans-serif;font-weight:900;color:var(--brand);text-transform:uppercase}
.intro-heading{left:470px;top:461px;font-size:33px;line-height:45px}
.intro-text{left:470px;top:557px;width:470px;font-size:21px;line-height:31px;font-weight:500}
.lose-heading{left:202px;top:716px;font-size:35px;line-height:43px}
.body{font-size:17px;line-height:29.6px}
.lose-text{left:202px;top:810px;width:440px}
.teeth-art{left:677px;top:731px;width:321px;height:274px;background:linear-gradient(135deg,#e8f1f8,#cadeef);border-radius:12px}
.rule{height:2px;background:var(--rule)}
.brush-art{left:205px;top:1046px;width:266px;height:242px;background:linear-gradient(135deg,#e8f1f8,#cadeef);border-radius:12px}
.clean-text{left:525px;top:1038px;width:470px;font-size:17px;line-height:26.5px}
.clean-text p{margin-bottom:12px}
.quote{left:202px;top:1338px;width:330px;font-family:"Montserrat",sans-serif;font-weight:700;font-size:21.5px;line-height:36px;color:var(--brand)}
.divider-v{left:583px;top:1348px;width:2px;height:376px;background:var(--rule)}
.tablets-heading{left:202px;top:1545px;font-size:32px;line-height:40px}
.tablets-text{left:202px;top:1594px;width:380px;font-size:17px;line-height:26.5px}
.why-heading{left:620px;top:1347px;font-size:33px;line-height:35px}
.why-text{left:620px;top:1430px;width:375px;font-size:17px;line-height:26.4px}
.warn-heading{left:421px;top:1797px;font-size:33px;line-height:40px}
.warn-text{left:421px;top:1844px;width:580px;font-size:17.3px;line-height:26px}
.contact{left:216px;top:2032px;font-size:18px;line-height:26.5px}
.logo-name{left:620px;top:2058px;font-family:"Inter",sans-serif;font-weight:700;font-size:33px;color:var(--logo-grey);letter-spacing:-0.5px}
.footer-band{left:125px;top:2168px;width:950px;height:18px;background:var(--brand)}
</style>
</head>
<body>
<div class="card"></div>
<div class="abs header-band"></div>
<svg class="abs header-pointer" width="52" height="26" viewBox="0 0 52 26"><polygon points="0,0 52,0 26,26" fill="#009ddc"/></svg>
<h1 class="abs page-title">LOOKING AFTER YOUR<br>RETAINERSAINERS</h1>

<section class="abs intro-box"></section>
<svg class="abs" style="left:250px;top:455px" width="170" height="195" viewBox="0 0 170 195" fill="none" stroke="#009ddc" stroke-width="5" stroke-linecap="round">
  <circle cx="85" cy="102" r="78"/>
  <circle cx="85" cy="102" r="62"/>
  <rect x="74" y="4" width="22" height="12" rx="3"/>
  <line x1="85" y1="16" x2="85" y2="24"/>
  <path d="M22 50 L12 40 L30 24 L40 34"/>
  <path d="M148 50 L158 40 L140 24 L130 34"/>
  <line x1="40" y1="168" x2="30" y2="186"/>
  <line x1="130" y1="168" x2="140" y2="186"/>
  <line x1="85" y1="102" x2="85" y2="58"/>
  <line x1="85" y1="102" x2="116" y2="102"/>
  <line x1="85" y1="102" x2="60" y2="128"/>
  <circle cx="85" cy="102" r="7"/>
  <g stroke-width="4">
    <line x1="85" y1="46" x2="85" y2="49"/><line x1="85" y1="155" x2="85" y2="158"/>
    <line x1="29" y1="102" x2="32" y2="102"/><line x1="138" y1="102" x2="141" y2="102"/>
    <line x1="57" y1="54" x2="58" y2="56"/><line x1="113" y1="54" x2="112" y2="56"/>
    <line x1="37" y1="74" x2="39" y2="75"/><line x1="133" y1="74" x2="131" y2="75"/>
    <line x1="37" y1="130" x2="39" y2="129"/><line x1="133" y1="130" x2="131" y2="129"/>
    <line x1="57" y1="150" x2="58" y2="148"/><line x1="113" y1="150" x2="112" y2="148"/>
  </g>
</svg>
<h2 class="abs heading intro-heading">The braces are off...<br>It’s retainer time!!!!</h2>
<p class="abs intro-text">Always wear your retainer as instructed by your orthodontist. Remember to take your retainer out when eating and playing sport</p>

<h2 class="abs heading lose-heading">Do not lose<br>your retainer!!!</h2>
<p class="abs body lose-text">The cost of your first retainers is covered in the fee for your treatment. However, if they are lost or broken and need replacement, this will incur an additional fee of $300 for a new one and we will have to take a new impression, So please look after it!!!! <strong>Always store in the retainer container provided</strong></p>
<div class="abs teeth-art" role="img" aria-label="Line drawing of a clear retainer over a set of teeth with fingers fitting it"></div>

<div class="abs rule" style="left:202px;top:1019px;width:796px"></div>

<div class="abs brush-art" role="img" aria-label="Line drawing of a toothbrush"></div>
<div class="abs clean-text">
  <p>Clean your Retainer regularly, using a tooth brush and soaking it in a retainer cleaner such as- Fresheze, or any denture cleaning tablet.</p>
  <p>If it is not fitting, call us to arrange to have it checked and adjusted. Always go to your retainer check appointments, and we will tighten the retainer.</p>
  <p><strong>So don’t forget your RETAINER!!!</strong></p>
</div>

<div class="abs rule" style="left:202px;top:1308px;width:796px"></div>

<p class="abs quote">If you want to keep your teeth straight never throw your retainers away! It’s up to you from here on...</p>
<div class="abs rule" style="left:202px;top:1511px;width:343px"></div>
<h2 class="abs heading tablets-heading">Cleaning tablets</h2>
<p class="abs tablets-text">Drop one tablet into enough warm (Not Hot) water to cover the appliance place appliance into the bubbling solution Leave for 10-15 mins and appliance is clean and odor free rinse thoroughly with running water</p>

<div class="abs divider-v"></div>

<h2 class="abs heading why-heading">Why is this<br>needed?</h2>
<p class="abs why-text">Long-term clinical research shows that no matter how well teeth are straightened, they will show a tendency for some movement over many years (probably throughout life). By the way, this also occurs with teeth that haven’t had any orthodontic treatment. This tooth movement often shows up as an increase in crowding of the front teeth, by trying your retainers in every so often- and if neces- sary wearing them occasionally- you can keep your teeth straight for the years ahead.</p>

<div class="abs rule" style="left:202px;top:1766px;width:796px"></div>

<svg class="abs" style="left:200px;top:1798px" width="130" height="120" viewBox="0 0 130 120" fill="none" stroke="#009ddc" stroke-width="6" stroke-linecap="round" stroke-linejoin="round">
  <path d="M56 10 Q65 -2 74 10 L124 100 Q128 114 112 114 L18 114 Q2 114 6 100 Z"/>
  <line x1="65" y1="40" x2="65" y2="80"/>
  <circle cx="65" cy="96" r="2" fill="#009ddc"/>
</svg>
<h2 class="abs heading warn-heading">Warnings</h2>
<p class="abs warn-text"><strong>Do not place tablets in mouth.</strong> Do not use to clean natural teeth, Keep product out of reach of children. In case of accidental ingestion seek professional assistance or contact poison centre immediately 13-00-000</p>

<div class="abs rule" style="left:202px;top:1962px;width:796px"></div>

<address class="abs contact" style="font-style:normal">48 Harbour Lane<br>LINDEN PARK VIC 3999<br>Phone: 9000 1234<br>Email: hello@northvale-ortho.com.au</address>
<div class="abs logo-name">Northvale Orthodontics</div>

<div class="abs footer-band"></div>
</body>
</html>
```